fizzy drinks label design

I want to design fizzy drink label for 3 flavors : black grapes, red apple and mojito, band name kestrola, product name KOLTA , product will be in plastic bottle, label size 198 mm X 66mm

```html
<!DOCTYPE html>
<html lang="en">
<head>
<meta charset="utf-8">
<title>KOLTA Flavour Labels</title>
<link href="https://fonts.googleapis.com/css2?family=Fredoka:wght@500;700&display=swap" rel="stylesheet">
<style>
  :root {
    --page-bg: #ececf1;
    --ink-light: #ffffff;

    --grape-deep: #6b22a8;
    --grape-mid: #a23fc9;
    --grape-glow: #f0a6e4;
    --grape-pill: #5a1f86;
    --grape-fruit-dark: #262a58;
    --grape-fruit-mid: #4d5392;
    --grape-splash: #f6c7ee;

    --apple-deep: #a3121c;
    --apple-mid: #d8323a;
    --apple-glow: #ff9c8c;
    --apple-pill: #7d0d15;
    --apple-fruit-dark: #8c0f18;
    --apple-fruit-mid: #e0433c;
    --apple-splash: #ffd0c6;

    --mojito-deep: #1f7a3a;
    --mojito-mid: #3fae55;
    --mojito-glow: #c4f0a0;
    --mojito-pill: #175c2b;
    --mojito-fruit-dark: #3c8a2a;
    --mojito-fruit-mid: #a6d94a;
    --mojito-splash: #e3f8cf;
  }
  * { margin: 0; padding: 0; box-sizing: border-box; }
  html, body {
    width: 900px;
    height: 1200px;
    overflow: hidden;
    background: var(--page-bg);
    font-family: "Fredoka", sans-serif;
  }
  .canvas {
    width: 900px;
    height: 1200px;
    display: flex;
    flex-direction: column;
    align-items: center;
    justify-content: center;
    gap: 28px;
  }
  .label {
    --deep: var(--grape-deep);
    --mid: var(--grape-mid);
    --glow: var(--grape-glow);
    --pill: var(--grape-pill);
    --fruit-dark: var(--grape-fruit-dark);
    --fruit-mid: var(--grape-fruit-mid);
    --splash: var(--grape-splash);
    position: relative;
    width: 780px;
    height: 352px;
    border-radius: 8px;
    overflow: hidden;
    display: flex;
    flex-direction: column;
    align-items: center;
    background:
      radial-gradient(ellipse 300px 190px at 50% 52%, var(--glow) 0%, var(--mid) 65%, transparent 100%),
      linear-gradient(90deg, var(--deep) 0%, var(--mid) 35%, var(--mid) 65%, var(--deep) 100%);
    box-shadow: 0 10px 28px rgba(40, 20, 60, 0.22);
  }
  .label--apple {
    --deep: var(--apple-deep);
    --mid: var(--apple-mid);
    --glow: var(--apple-glow);
    --pill: var(--apple-pill);
    --fruit-dark: var(--apple-fruit-dark);
    --fruit-mid: var(--apple-fruit-mid);
    --splash: var(--apple-splash);
  }
  .label--mojito {
    --deep: var(--mojito-deep);
    --mid: var(--mojito-mid);
    --glow: var(--mojito-glow);
    --pill: var(--mojito-pill);
    --fruit-dark: var(--mojito-fruit-dark);
    --fruit-mid: var(--mojito-fruit-mid);
    --splash: var(--mojito-splash);
  }
  .brand {
    margin-top: 18px;
    display: flex;
    align-items: center;
    gap: 7px;
    color: var(--ink-light);
    font-weight: 700;
    font-size: 19px;
    line-height: 1;
  }
  .brand-dot {
    width: 11px;
    height: 11px;
    border-radius: 50%;
    background: var(--ink-light);
  }
  .product-name {
    margin-top: 4px;
    color: var(--ink-light);
    font-weight: 700;
    font-size: 84px;
    line-height: 1;
    letter-spacing: 2px;
  }
  .flavour-pill {
    margin-top: 6px;
    padding: 4px 18px;
    border-radius: 14px;
    background: var(--pill);
    color: var(--ink-light);
    font-weight: 500;
    font-size: 17px;
    line-height: 1.2;
  }
  .fruit-art {
    margin-top: 10px;
    width: 100%;
    height: 128px;
    background:
      radial-gradient(ellipse 120px 60px at 50% 50%, var(--fruit-mid) 0%, var(--fruit-dark) 85%, transparent 100%),
      radial-gradient(ellipse 390px 46px at 50% 72%, var(--splash) 0%, transparent 100%);
  }
  .volume {
    position: absolute;
    bottom: 12px;
    color: var(--ink-light);
    font-weight: 500;
    font-size: 16px;
    line-height: 1;
  }
</style>
</head>
<body>
  <main class="canvas">
    <section class="label label--grape">
      <div class="brand"><span class="brand-dot"></span>kestrola</div>
      <h1 class="product-name">KOLTA</h1>
      <div class="flavour-pill">Black Grape</div>
      <div class="fruit-art" role="img" aria-label="Bunch of black grapes over a light juice splash"></div>
      <div class="volume">500ml</div>
    </section>
    <section class="label label--apple">
      <div class="brand"><span class="brand-dot"></span>kestrola</div>
      <h2 class="product-name">KOLTA</h2>
      <div class="flavour-pill">Red Apple</div>
      <div class="fruit-art" role="img" aria-label="Red apples over a light juice splash"></div>
      <div class="volume">500ml</div>
    </section>
    <section class="label label--mojito">
      <div class="brand"><span class="brand-dot"></span>kestrola</div>
      <h2 class="product-name">KOLTA</h2>
      <div class="flavour-pill">Mojito</div>
      <div class="fruit-art" role="img" aria-label="Lime slices and mint leaves over a light juice splash"></div>
      <div class="volume">500ml</div>
    </section>
  </main>
</body>
</html>
```